pharmacy/travel clinic business card design

We need a business card for our new business called Brenwick Travel Clinic and Pharmacy. Our primary focus is doing consultations for people before travelling internationally and providing vaccinations and prescriptions for them. While the business is considered a pharmacy, it has more the look and feel of a doctor's office. The design should communicate a professional and trustworthy feel. I have attached a copy of the logo we are going to be using.
Updates
Thanks for the submissions.  If you haven`t been eliminated you are one of the finalists.  Decision will likely be made tomorrow.

Target Market(s)
Customers, other health care professionals, travel agents
Industry/Entity Type
Clinic
Look and feel
Each slider illustrates characteristics of the customer's brand and the style your logo design should communicate.

```html
<!DOCTYPE html>
<html lang="en">
<head>
<meta charset="utf-8">
<title>Brenwick Travel Clinic and Pharmacy — Business Card</title>
<link rel="stylesheet" href="https://fonts.googleapis.com/css2?family=Gabriela&display=swap">
<style>
  :root {
    --backdrop: #2b1e14;
    --card-lime: #b6ef5c;
    --card-white: #ffffff;
    --panel-blue: #7fd2ec;
    --divider: #b3e5f3;
    --ink: #111111;
    --brand-blue: #2f74d4;
    --brand-light: #5fb0f0;
  }
  html, body {
    margin: 0;
    padding: 0;
    width: 922px;
    height: 1200px;
    overflow: hidden;
    background: var(--backdrop);
  }
  .canvas {
    display: block;
    width: 922px;
    height: 1200px;
  }
  .card-base { fill: url(#cardFade); }
  .panel { fill: var(--panel-blue); }
  .divider { stroke: var(--divider); stroke-width: 1.5; }
  .text {
    font-family: "Gabriela", serif;
    fill: var(--ink);
  }
  .name { font-size: 25px; }
  .title { font-size: 25px; }
  .brand-block { font-size: 18px; }
  .contact { font-size: 21px; }
  .brand-name {
    font-family: "Gabriela", serif;
    fill: var(--brand-blue);
  }
  .brand-mark { fill: var(--brand-blue); }
  .lockup-name {
    font-family: "Gabriela", serif;
    fill: var(--brand-light);
  }
  .icon-fill { fill: var(--ink); }
  .icon-line { fill: none; stroke: var(--ink); stroke-width: 2.4; }
  .icon-cut { fill: var(--panel-blue); }
</style>
</head>
<body>
<svg class="canvas" viewBox="0 0 787 1024" width="922" height="1200" xmlns="http://www.w3.org/2000/svg">
  <defs>
    <linearGradient id="cardFade" x1="0" y1="0" x2="0" y2="1">
      <stop offset="0" stop-color="var(--card-lime)"/>
      <stop offset="0.55" stop-color="#dff8c2"/>
      <stop offset="1" stop-color="var(--card-white)"/>
    </linearGradient>
  </defs>

  <!-- Business card -->
  <g class="business-card">
    <rect class="card-base" x="46" y="152" width="718" height="504" rx="6"/>

    <!-- Upper panel: name and brand -->
    <path class="panel" d="M82,390 L82,265 Q92,182 215,178 L733,180 L733,312 Q702,386 585,390 Z"/>
    <text class="text name" x="162" y="272">Your Name Here</text>
    <text class="text title" x="218" y="311">Title</text>

    <g class="brand-top">
      <text class="brand-name" x="432" y="245" font-size="34">Brenwick</text>
      <text class="brand-name" x="452" y="288" font-size="34">Travel Clinic</text>
      <text class="brand-name" x="462" y="322" font-size="19">and Pharmacy</text>
    </g>

    <!-- Lower panel: brand and contact -->
    <path class="panel" d="M82,422 L600,422 Q718,428 733,500 L733,632 L225,634 Q95,624 82,560 Z"/>

    <g class="brand-block-group">
      <circle class="brand-mark" cx="138" cy="530" r="22"/>
      <text class="text brand-block" x="176" y="518">BRENWICK</text>
      <text class="text brand-block" x="200" y="548">TRAVEL CLINIC</text>
      <text class="text brand-block" x="218" y="577">AND PHARMACY</text>
    </g>

    <line class="divider" x1="393" y1="462" x2="393" y2="582"/>

    <g class="contact-list">
      <!-- address -->
      <g class="icon-home">
        <path class="icon-fill" d="M446,461 L466,479 L461,479 L461,497 L451,497 L451,487 L441,487 L441,497 L431,497 L431,479 L426,479 Z"/>
      </g>
      <text class="text contact" x="474" y="492">Your address here</text>

      <!-- email -->
      <g class="icon-mail">
        <rect class="icon-fill" x="428" y="517" width="36" height="30" rx="4"/>
        <rect fill="#ffffff" x="433" y="522" width="26" height="20"/>
        <path class="icon-line" d="M433,522 L446,534 L459,522 M433,542 L442,531 M459,542 L450,531" stroke-width="1.6"/>
      </g>
      <text class="text contact" x="478" y="540">hello@brenwickmail.com</text>

      <!-- phone -->
      <g class="icon-phone">
        <circle class="icon-line" cx="447" cy="579" r="16"/>
        <path class="icon-fill" d="M441,569 Q438,571 439,576 Q442,586 452,590 Q456,591 458,588 L454,584 L451,586 Q446,583 444,578 L446,575 Z"/>
      </g>
      <text class="text contact" x="482" y="587">041286730</text>
    </g>
  </g>

  <!-- Brand lockup beneath the card -->
  <g class="brand-lockup">
    <text class="lockup-name" x="330" y="915" font-size="52">Brenwick</text>
    <text class="lockup-name" x="338" y="972" font-size="54">Travel Clinic</text>
    <text class="lockup-name" x="350" y="1002" font-size="24">and Pharmacy</text>
  </g>
</svg>
</body>
</html>
```